Tri-fold brochue, business card, and stationary design.

Tri-fold brochure: We are looking to get a tri-fold brochure template created so we can add our content on each side of the brochure and then leave these with prospective clients during sales calls.Business card: We would like the business card to have employee name, phone number, and email address on the card. We are open to rounded corners as well.We just redid our website and we'd like all designs to be complementary to our new "Look and feel" of our website.

Contact Information for Business Card

We would like the business card to have employee name, phone number, and email address on the card. We are open to rounded corners as well.

We just redid our website and we'd like all designs to be complementary to our new "Look and feel" of our website.

```html
<!DOCTYPE html>
<html lang="en">
<head>
<meta charset="utf-8">
<title>Harborline Networks – Tri-fold Brochure</title>
<link href="https://fonts.googleapis.com/css2?family=Nunito+Sans:wght@400;600;700;800&display=swap" rel="stylesheet">
<style>
:root{
  --blue:#1a8fd6;
  --blue-deep:#0b5f9e;
  --blue-navy:#063a66;
  --dark:#1c1d1f;
  --dark-2:#262729;
  --white:#ffffff;
  --ink:#1b1b1b;
  --page:#f1f1f1;
}
*{box-sizing:border-box;margin:0;padding:0}
html,body{width:1200px;height:1000px;overflow:hidden}
body{background:var(--page);font-family:"Nunito Sans",Arial,sans-serif;position:relative;color:var(--white)}
.sheet{position:absolute;left:289px;width:627px;box-shadow:0 4px 14px rgba(0,0,0,.18)}
.sheet-outside{top:7px;height:482px}
.sheet-inside{top:502px;height:483px;background:var(--white)}
.abs{position:absolute}

/* outside */
.panel-whatif{left:0;top:0;width:210px;height:482px;background:linear-gradient(180deg,#1a86c8 0%,#0f6aa8 45%,#0a4c80 75%,#0b3f6b 100%)}
.panel-whatif h2{position:absolute;left:15px;top:22px;font-size:16px;font-weight:800;letter-spacing:.3px}
.whatif-list{position:absolute;left:25px;top:56px;width:170px;list-style:none;font-size:9.2px;line-height:11.5px}
.whatif-list li{position:relative;padding-left:14px;margin-bottom:11px}
.whatif-list li::before{content:"";position:absolute;left:2px;top:4px;width:4px;height:4px;border-radius:50%;background:var(--white)}
.whatif-art{left:0;top:220px;width:210px;height:262px;background:radial-gradient(circle at 40% 45%,rgba(60,170,230,.45),rgba(10,60,100,0) 65%)}

.panel-reasons-photo{left:210px;top:0;width:208px;height:360px;background:linear-gradient(180deg,#c9d4dc,#9fb2c0 60%,#8597a6)}
.reasons-box{left:224px;top:7px;width:177px;height:348px;background:rgba(26,143,214,.88)}
.reasons-box h2{text-align:center;font-size:13px;font-weight:800;line-height:16px;margin-top:25px}
.reasons-list{list-style:none;margin:10px 12px 0 30px;font-size:9px;line-height:11.3px;text-align:justify}
.reasons-list li{position:relative;margin-bottom:11px}
.reasons-list li::before{content:"";position:absolute;left:-16px;top:3px;width:5px;height:5px;border-right:1.6px solid var(--white);border-top:1.6px solid var(--white);transform:rotate(45deg)}

.panel-contact{left:210px;top:360px;width:208px;height:122px;background:var(--dark-2);text-align:center}
.panel-contact h2{color:var(--blue);font-size:14px;font-weight:800;margin-top:12px;letter-spacing:.3px}
.contact-icon{display:block;margin:4px auto 2px;width:10px;height:10px}
.contact-line{font-size:8px;line-height:10px}
.contact-line.phone{font-weight:800;font-size:8.5px}

.panel-cover-photo{left:418px;top:0;width:209px;height:360px;background:linear-gradient(160deg,#e9ebed 0%,#cfd4d8 45%,#7c838a 80%,#4a4f55 100%)}
.tagline{left:453px;top:0;width:137px;height:69px;background:var(--blue);text-align:center;padding-top:27px}
.tagline .small{font-size:9.5px;font-weight:800;letter-spacing:.2px}
.tagline .big{font-size:14px;font-weight:600}
.panel-brand{left:418px;top:360px;width:209px;height:122px;background:var(--dark)}
.brand{position:absolute;left:30px;top:44px;display:flex;align-items:center;gap:8px}
.brand-mark{width:22px;height:22px;background:var(--blue)}
.brand-name{color:var(--blue);font-size:17px;font-weight:800;line-height:18px}

/* inside */
.panel-story{left:0;top:0;width:210px;height:483px;background:linear-gradient(180deg,#1e1f21,#262729 55%,#1a1b1d)}
.section-title{position:absolute;font-size:16px;font-weight:800;display:flex;align-items:center}
.section-title::before{content:"";width:14px;height:11px;background:var(--blue);margin-right:6px;margin-left:-4px}
.section-title .accent{color:var(--blue);margin-right:5px}
.story-text{position:absolute;left:20px;top:57px;width:187px;font-size:8.8px;line-height:10.6px;font-weight:700;text-align:justify}
.story-text p+p{margin-top:9px}
.why-list{position:absolute;left:20px;top:250px;width:182px;list-style:none}
.why-list li{position:relative;padding-left:21px;margin-bottom:6px;font-size:8.6px;line-height:10.4px;text-align:justify}
.why-list h3{font-size:9.2px;font-weight:800;line-height:11px}
.why-list svg{position:absolute;left:0;top:0;width:13px;height:13px}

.inside-photo{left:210px;top:0;width:417px;height:206px;background:radial-gradient(ellipse at 55% 55%,#3a9bd8 0%,#124f86 40%,#0a2039 80%)}
.support-band{left:210px;top:215px;width:417px;height:66px;background:var(--blue)}
.support-band h2{position:absolute;left:12px;top:8px;color:var(--ink);font-size:21px;font-weight:800;line-height:23px;letter-spacing:.2px}
.support-band .rule{position:absolute;left:187px;top:8px;width:2px;height:50px;background:var(--ink)}
.support-band p{position:absolute;left:198px;top:7px;width:212px;font-size:9.2px;line-height:11.2px;text-align:justify}
.services{left:210px;top:281px;width:417px;height:202px;color:var(--ink)}
.services .section-title{left:14px;top:16px}
.service{position:absolute;width:150px;font-size:8.6px;line-height:10.3px;text-align:justify}
.service h3{font-size:8.8px;font-weight:800}
.service-icon{position:absolute;width:28px;height:28px}
.services-rule{position:absolute;left:0;bottom:10px;width:417px;height:4px;background:var(--blue)}
</style>
</head>
<body>

<section class="sheet sheet-outside" aria-label="Brochure outside">
  <div class="abs panel-whatif">
    <h2>WHAT IF.....</h2>
    <ul class="whatif-list">
      <li>I could communicate with my IT support company.</li>
      <li>I could work from home if I needed to and it be just like when I am in the office.</li>
      <li>I could actually have a disaster recovery plan that I know how it works.</li>
      <li>I could determine what messages</li>
    </ul>
    <div class="abs whatif-art" role="img" aria-label="Digital security graphic with glowing circuit rings and a shield"></div>
  </div>

  <div class="abs panel-reasons-photo" role="img" aria-label="Blurred office photograph behind the reasons list"></div>
  <div class="abs reasons-box">
    <h2>TOP REASONS TO<br>CALL HARBORLINE NOW</h2>
    <ul class="reasons-list">
      <li>Need Local IT Support</li>
      <li>Would like to have an IT professional provide help when needed.</li>
      <li>I need to update my IT security but not sure how.</li>
      <li>I need a plan to replace EOL Orbit 7 machines in my network.</li>
      <li>I need help with emergency service and not sure who to call if something happens to my network.</li>
      <li>I have no Business Continuity plan.</li>
      <li>Is the cloud a good move for our organization. What does it cost to move.</li>
    </ul>
  </div>
  <div class="abs panel-contact">
    <h2>CONTACT US</h2>
    <svg class="contact-icon" viewBox="0 0 10 10"><circle cx="5" cy="5" r="5" fill="#1a8fd6"/><path d="M3.3 2.6l1 1-.5.6a3 3 0 0 0 2 2l.6-.5 1 1-.7.7C5 7.3 2.7 5 2.6 3.3z" fill="#262729"/></svg>
    <p class="contact-line phone">555-014-2370</p>
    <svg class="contact-icon" viewBox="0 0 10 10"><circle cx="5" cy="5" r="5" fill="#1a8fd6"/><path d="M2.5 5h5M5 2.5c1.2 1.4 1.2 3.6 0 5M5 2.5c-1.2 1.4-1.2 3.6 0 5" stroke="#262729" stroke-width=".7" fill="none"/></svg>
    <p class="contact-line">dana@harborlinenet.com</p>
    <svg class="contact-icon" viewBox="0 0 10 10"><circle cx="5" cy="5" r="5" fill="#1a8fd6"/><path d="M5 2.2a1.8 1.8 0 0 1 1.8 1.8C6.8 5.3 5 7.6 5 7.6S3.2 5.3 3.2 4A1.8 1.8 0 0 1 5 2.2z" fill="#262729"/></svg>
    <p class="contact-line">1420 Larkfield Court Suite B</p>
    <p class="contact-line">Ashby, OH 43990</p>
  </div>

  <div class="abs panel-cover-photo" role="img" aria-label="Photograph of a business team working together at laptops"></div>
  <div class="abs tagline">
    <p class="small">MANAGING NETWORKS:</p>
    <p class="big">Impacting Lives.</p>
  </div>
  <div class="abs panel-brand">
    <div class="brand"><span class="brand-mark"></span><span class="brand-name">Harborline Networks</span></div>
  </div>
</section>

<section class="sheet sheet-inside" aria-label="Brochure inside">
  <div class="abs panel-story">
    <h2 class="section-title" style="left:4px;top:28px"><span class="accent">OUR</span>STORY</h2>
    <div class="story-text">
      <p>Lorem ipsum dolor sit amet, consectetur adipiscing elit. Morbi tincidunt id libero vel venenatis. Nam id tortor sed ex iaculis varius id a tortor. Sed vitae elementum ex. Mauris ac lacus ac nisl efficitur suscipit. Morbi et est felis. Nulla in augue ut ligula gravida vehicula eget nec erat. Etiam laoreet vitae ligula eget auctor.</p>
      <p>Phasellus eget maximus nulla. Quisque blandit eleifend rhoncus. Morbi dictum lectus quis feugiat blandit. Sed venenatis nibh sed nunc lobortis, ut aliquam tortor condimentum.</p>
    </div>
    <h2 class="section-title" style="left:4px;top:216px"><span class="accent">WHY</span>CHOOSE US?</h2>
    <ul class="why-list">
      <li><svg viewBox="0 0 13 13"><circle cx="6" cy="7" r="5.3" fill="none" stroke="#1a8fd6" stroke-width="1.3"/><path d="M3.5 6.8l2.3 2.3L12 2" fill="none" stroke="#1a8fd6" stroke-width="1.6"/></svg><h3>AFFORDABLE</h3>With flat-rate pricing, we keep your office running smoothly at a fraction of the cost when compared to traditional IT options.</li>
      <li><svg viewBox="0 0 13 13"><circle cx="6" cy="7" r="5.3" fill="none" stroke="#1a8fd6" stroke-width="1.3"/><path d="M3.5 6.8l2.3 2.3L12 2" fill="none" stroke="#1a8fd6" stroke-width="1.6"/></svg><h3>COMPREHENSIVE</h3>From the network-level down to the device-level, we offer as much or as little IT support as you need-but we'll always go beyond the call of duty.</li>
      <li><svg viewBox="0 0 13 13"><circle cx="6" cy="7" r="5.3" fill="none" stroke="#1a8fd6" stroke-width="1.3"/><path d="M3.5 6.8l2.3 2.3L12 2" fill="none" stroke="#1a8fd6" stroke-width="1.6"/></svg><h3>LIGHTNING QUICK</h3>We know your time is important to you— especially when WiFi is down— and we actually care.</li>
      <li><svg viewBox="0 0 13 13"><circle cx="6" cy="7" r="5.3" fill="none" stroke="#1a8fd6" stroke-width="1.3"/><path d="M3.5 6.8l2.3 2.3L12 2" fill="none" stroke="#1a8fd6" stroke-width="1.6"/></svg><h3>ON-SITE SUPPORT</h3>Need something that can't be provided remotely or is unique to your business or industry? Let our experts help.</li>
    </ul>
  </div>

  <div class="abs inside-photo" role="img" aria-label="Photograph of glowing blue network light trails over a night city"></div>
  <div class="abs support-band">
    <h2>HOW DO WE<br>SUPPORT YOU?</h2>
    <span class="rule"></span>
    <p>As long as employees can't remember their passwords, move offices, get hired, get fired, and more, Harborline Networks will be standing by — by phone, email, or at your office.</p>
  </div>

  <div class="abs services">
    <h2 class="section-title"><span class="accent">OUR</span>SERVICES</h2>

    <svg class="service-icon" style="left:18px;top:60px" viewBox="0 0 28 28"><path d="M7 3h14v22l-7-6-7 6z" fill="none" stroke="#1a8fd6" stroke-width="2"/></svg>
    <div class="service" style="left:59px;top:53px"><h3>MANAGED SERVICES</h3>Reduce stress, improve efficiency, and increase profit. Our team will streamline and manage the day-to-day technology for you</div>

    <svg class="service-icon" style="left:18px;top:130px" viewBox="0 0 28 28"><rect x="3" y="6" width="22" height="16" rx="3" fill="none" stroke="#1a8fd6" stroke-width="2"/><path d="M3 14h22" stroke="#1a8fd6" stroke-width="2"/><path d="M7 18h2M11 18h2" stroke="#1a8fd6" stroke-width="2"/></svg>
    <div class="service" style="left:59px;top:118px"><h3>SKYVAULT CLOUD</h3>Access your data from anywhere, at any time. Our team knows Skyvault and knows the huge benefit the cloud can provide. Let us show how to migrate to the cloud</div>

    <svg class="service-icon" style="left:220px;top:58px" viewBox="0 0 28 28"><path d="M14 4C7.4 4 3 8 3 12.5c0 2.6 1.5 4.8 3.8 6.3L5.5 24l5.3-3.2c1 .2 2.1.3 3.2.3 6.6 0 11-4 11-8.6S20.6 4 14 4z" fill="none" stroke="#1a8fd6" stroke-width="2"/><circle cx="9.5" cy="12.5" r="1.5" fill="#1a8fd6"/><circle cx="14" cy="12.5" r="1.5" fill="#1a8fd6"/><circle cx="18.5" cy="12.5" r="1.5" fill="#1a8fd6"/></svg>
    <div class="service" style="left:263px;top:53px"><h3>WORKDESK SUITE</h3>Access your email, documents, contacts and calendar from almost anywhere with any device and work smarter, not harder</div>

    <svg class="service-icon" style="left:220px;top:128px" viewBox="0 0 28 28"><path d="M3 7h8l2 3h12v13H3z" fill="none" stroke="#1a8fd6" stroke-width="2"/><path d="M3 23l4-9h21l-3 9" fill="none" stroke="#1a8fd6" stroke-width="2"/></svg>
    <div class="service" style="left:263px;top:120px"><h3>BACKUP &amp; BUSINESS CONTINUITY</h3>Protect everything you and your company have worked hard for! Our team is committed to providing the best solutions for the safety and security of your data!</div>

    <span class="services-rule"></span>
  </div>
</section>

</body>
</html>
```